Young Accounting firm needing a captivating business card

We need a business card design that forces the person to look at the card because its either gold foil, plastic, or lettering pop up etc. We already have a logo with a specific gold color and we need to make it pop. We are an accounting firm. I need the words" accounting, payroll, licenses, audits, taxes" somewhere on the business card so as to describe what we do- preferably on the side where the logo is at.

Industry/Entity Type

Accounting

Contact Information for Business Card

Address 48276 9th Ave S Ste 305, Federal Way, WA 98117
Business Phone (360)418-2096
Fax (360)418-2157
Office Cell Phone (360)586-7319

Font styles to use
Serif

Colors
85abd2

Requirements
Must have
• It should state
• "Accounting" "Taxes" "Audits" "Licenses" "Payroll"
Nice to have
• Matte with gold foil, different textures, With Either a textured ivory background or gray blue slate background
Should not have
• colorful colors

```html
<!DOCTYPE html>
<html lang="en">
<head>
<meta charset="utf-8">
<title>KLTaxworks Business Card</title>
<link href="https://fonts.googleapis.com/css2?family=Arimo:wght@400;700&display=swap" rel="stylesheet">
<style>
  :root {
    --backdrop: #3a3b3e;
    --amber: #f2ab2a;
    --amber-light: #fdc756;
    --amber-deep: #e99e1e;
    --ink: #4a4a4c;
    --gold: #b8a22c;
    --divider: #d9a73a;
  }
  * { margin: 0; padding: 0; box-sizing: border-box; }
  html, body { width: 1200px; height: 900px; overflow: hidden; }
  body {
    background: var(--backdrop);
    font-family: "Arimo", Arial, sans-serif;
    color: var(--ink);
    position: relative;
  }
  .card {
    position: absolute;
    left: 240px;
    width: 720px;
    height: 411px;
    overflow: hidden;
    box-shadow: 0 10px 24px rgba(0,0,0,.45);
  }
  .card--front { top: 26px; }
  .card--back { top: 463px; }
  .card__surface {
    position: absolute; inset: 0;
    background: linear-gradient(135deg, var(--amber-light) 0%, var(--amber) 45%, var(--amber-deep) 100%);
  }
  .brand {
    position: absolute;
    display: flex; align-items: center; gap: 12px;
    font-weight: 700;
    white-space: nowrap;
  }
  .brand__mark { background: currentColor; flex: none; }
  .card--front .brand {
    left: 60px; top: 178px;
    font-size: 40px; color: var(--ink);
  }
  .card--front .brand__mark { width: 22px; height: 22px; }
  .divider {
    position: absolute; left: 350px; top: 70px;
    width: 3px; height: 220px; background: var(--divider);
  }
  .contacts {
    position: absolute; left: 390px; top: 82px;
    list-style: none;
  }
  .contacts li {
    display: flex; align-items: center; gap: 16px;
    font-size: 22px; font-weight: 700; height: 46px;
  }
  .contacts svg { width: 22px; height: 22px; flex: none; fill: var(--ink); }
  .address {
    position: absolute; left: 0; right: 0; bottom: 46px;
    text-align: center; font-size: 22px; font-weight: 700;
  }
  .card--back .brand {
    left: 0; right: 0; top: 130px; justify-content: center;
    font-size: 72px; color: var(--gold);
  }
  .card--back .brand__mark { width: 34px; height: 34px; }
  .services {
    position: absolute; left: 0; right: 0; bottom: 52px;
    display: flex; justify-content: center; gap: 14px;
    list-style: none;
    font-size: 19px; font-weight: 700; letter-spacing: .5px;
  }
  .services li { display: flex; align-items: center; gap: 7px; }
  .services li::before {
    content: ""; width: 10px; height: 10px; background: var(--ink);
  }
</style>
</head>
<body>
  <section class="card card--front">
    <div class="card__surface" role="img" aria-label="Amber diamond checker pattern"></div>
    <div class="brand"><span class="brand__mark"></span>KLTaxworks</div>
    <div class="divider"></div>
    <ul class="contacts">
      <li>
        <svg viewBox="0 0 24 24" aria-label="Phone"><path d="M3 9c0-3 4-5 9-5s9 2 9 5v2h-5V8.5c-2-.7-6-.7-8 0V11H3z"/><path d="M6 12h12l2 8H4z"/></svg>
        (360)418-2096
      </li>
      <li>
        <svg viewBox="0 0 24 24" aria-label="Fax"><path d="M7 2h8l3 3v5H7z" fill="none" stroke="#4a4a4c" stroke-width="2"/><rect x="3" y="11" width="18" height="10" rx="1"/></svg>
        (360)418-2157
      </li>
      <li>
        <svg viewBox="0 0 24 24" aria-label="Mobile"><rect x="7" y="2" width="10" height="20" rx="2"/><rect x="9" y="5" width="6" height="8" fill="#f2ab2a"/></svg>
        (360)586-7319
      </li>
      <li>
        <svg viewBox="0 0 24 24" aria-label="Email"><rect x="2" y="5" width="20" height="14"/><path d="M2 5l10 8 10-8" fill="none" stroke="#f2ab2a" stroke-width="2"/></svg>
        hello@kltaxworks.com
      </li>
    </ul>
    <p class="address">48276 9th Ave S Ste 305, Federal Way, WA 98117</p>
  </section>

  <section class="card card--back">
    <div class="card__surface" role="img" aria-label="Amber diamond checker pattern"></div>
    <div class="brand"><span class="brand__mark"></span>KLTaxworks</div>
    <ul class="services">
      <li>ACCOUNTING</li>
      <li>TAXES</li>
      <li>AUDITS</li>
      <li>LICENSES</li>
      <li>PAYROLL</li>
    </ul>
  </section>
</body>
</html>
```